Health & Fitness Retreat Homepage Design

We have an existing website at http://www.WillowBendHaven.com.au which we are retaining but wish to have a freshly designed homepage with the existing top navigation bar.
Sample layout is attached, but feel free to use your creativity on layout and colours, always remembering it needs to fit with the wider site design.
Project Delivery:
5 phase slide slow at top of homepage
Full homepage design and associated files
Target Audience:
- Female 80%, Male 20%
- Aged 30 to 50
- Overweight/Obese (so no pictures of thin people)
See attached layout for more information.
Target Market(s)
Target Audience:
- Female 80%, Male 20%
- Aged 30 to 50
Industry/Entity Type
Fitness
Requirements
Must have
- Must have existing top navigation bar as at http://www.WillowBendHaven.com.au and fit with existing interior colours, etc.
Should not have
- No pictures of thin people

```html
<!DOCTYPE html>
<html lang="en">
<head>
<meta charset="utf-8">
<title>WillowBendHaven – Weight Loss Retreat</title>
<link href="https://fonts.googleapis.com/css2?family=Arimo:wght@400;700&family=Oswald:wght@500;700&display=swap" rel="stylesheet">
<style>
:root{
  --orange:#f08a1c;
  --orange-light:#f7a54a;
  --orange-deep:#d9650c;
  --green:#7ab51d;
  --green-dark:#5d9410;
  --brown:#8a4a12;
  --text-orange:#c8650e;
  --hero-bg:#f4f4f4;
  --wood-a:#f3d3a0;
  --wood-b:#e9bd7c;
  --panel:#f9e7c9;
  --white:#ffffff;
  --grey:#777;
  --footer:#c96612;
}
*{margin:0;padding:0;box-sizing:border-box}
html,body{width:1200px;height:1091px;overflow:hidden}
body{font-family:"Arimo",Arial,sans-serif;position:relative;background:var(--hero-bg)}
.abs{position:absolute}

/* header */
.topbar{left:0;top:0;width:1200px;height:48px;background:linear-gradient(#f7a54a,#ee8a24)}
.brand{left:208px;top:0;width:192px;height:48px;background:var(--white);display:flex;align-items:center;padding-left:14px;gap:8px}
.brand-dot{width:20px;height:20px;border-radius:50%;background:var(--orange)}
.brand-name{font-size:16px;font-weight:700;color:var(--green)}
.member-login{left:400px;top:14px;width:75px;height:21px;background:var(--green);color:#fff;font-size:10px;line-height:21px;text-align:center;border-radius:2px}
.nav{left:688px;top:13px;display:flex;align-items:center}
.nav a{color:#fff;font-size:10px;text-decoration:none;height:22px;line-height:22px;padding:0 12px;margin-right:8px}
.nav a.active{background:var(--green);border-radius:2px;padding:0 12px}

/* hero */
.hero{left:0;top:48px;width:1200px;height:464px;background:repeating-linear-gradient(90deg,#f7f7f7 0 3px,#f1f1f1 3px 6px)}
.hero-photo{left:208px;top:48px;width:343px;height:464px;background:linear-gradient(120deg,#f6e6dc,#e8c3ad 55%,#f4ece8)}
.hero-kicker{left:590px;top:150px;font-size:28px;color:var(--orange)}
.hero-title{left:588px;top:172px;font-size:68px;color:var(--green);letter-spacing:-1px;white-space:nowrap}
.hero-title .amp{color:var(--orange);font-size:50px}
.hero-text{left:590px;top:244px;width:410px;font-size:11.5px;line-height:14.5px;color:var(--grey)}
.hero-text em{font-style:normal;color:var(--orange)}
.btn-brochure{left:840px;top:287px;width:151px;height:31px;background:linear-gradient(#8fc92b,#6ea715);color:#fff;font-size:14px;line-height:31px;text-align:center;border-radius:2px}
.thumb{top:358px;width:92px;height:92px;border-radius:50%;border:3px solid var(--orange-light)}
.thumb.t1{left:591px;background:linear-gradient(#f3ddd0,#dcb49b)}
.thumb.t2{left:693px;background:linear-gradient(#edc7ac,#d7a47f)}
.thumb.t3{left:796px;background:linear-gradient(#f7efe9,#dfa88d)}
.thumb.t4{left:898px;background:linear-gradient(#c9c9c9,#f4f4f4)}

/* wood section */
.wood{left:0;top:512px;width:1200px;height:512px;background:repeating-linear-gradient(90deg,var(--wood-a) 0 14px,var(--wood-b) 14px 18px,var(--wood-a) 18px 31px)}
.edge{left:0;width:1200px;height:8px}
.panel{background:rgba(252,236,210,.85);border-radius:3px;box-shadow:0 1px 3px rgba(120,60,0,.35)}
.about{left:208px;top:538px;width:542px;height:89px;padding:10px 12px}
.about h2{font-weight:400;font-size:19px;color:var(--brown)}
.about p{margin-top:4px;font-size:11px;line-height:14.5px;color:var(--text-orange);text-align:justify}
.visit{left:756px;top:538px;width:235px;height:89px;padding:12px 12px}
.visit .lead{font-size:14px;line-height:12px;color:var(--orange)}
.visit .lead b{display:block;font-weight:400;font-size:18px;line-height:18px}
.btn-join-now{left:132px;top:12px;width:90px;height:26px;background:var(--green);color:#fff;font-size:13px;line-height:26px;text-align:center;border-radius:2px}
.visit p{margin-top:12px;font-size:9px;line-height:12.5px;color:var(--brown)}

.card{top:633px;width:191px;height:199px;border-radius:3px;overflow:hidden;box-shadow:0 1px 3px rgba(120,60,0,.35);background:#fff}
.card-head{height:33px;background:rgba(247,220,178,.95);padding:6px 11px;font-size:11.5px;line-height:12px;color:var(--brown)}
.card-head.single{padding-top:10px;font-size:13px}
.card-body{padding:12px 11px 0}
.card-lead{display:flex;gap:8px;align-items:center}
.card-icon{flex:none;width:40px;height:40px;border-radius:50%;background:linear-gradient(#f8d9a8,#f0b567)}
.card-lead strong{font-size:9px;line-height:11px;color:var(--text-orange)}
.card-body p{margin-top:10px;font-size:8.3px;line-height:11.2px;color:var(--text-orange);text-align:justify}
.card-more{position:absolute;left:0;bottom:0;width:100%;height:22px;background:rgba(247,220,178,.95);font-size:8.5px;line-height:22px;text-align:right;padding-right:14px;color:var(--brown)}

.promo{left:208px;top:838px;width:389px;height:160px}
.promo-inner{left:12px;top:12px;width:365px;height:135px;background:#fff;overflow:hidden}
.promo-photo{left:0;top:0;width:140px;height:135px;background:linear-gradient(90deg,#f2e4dc,#e9cfc0 60%,#fff)}
.promo-title{left:143px;top:50px;font-family:"Oswald",sans-serif;font-weight:700;font-size:30px;line-height:32px;color:var(--green)}
.promo-sub{left:143px;top:81px;font-size:19px;color:var(--orange)}
.ribbon{left:258px;top:0;width:110px;height:110px}

.newsletter{left:602px;top:838px;width:389px;height:160px}
.newsletter-inner{left:12px;top:12px;width:365px;height:135px;background:#fff;padding:18px 14px}
.nl-title{font-size:19px;color:var(--orange);white-space:nowrap}
.nl-title b{font-family:"Oswald",sans-serif;font-weight:700;font-size:23px}
.nl-sub{margin-top:3px;font-size:11.5px;color:#666}
.nl-form{margin-top:12px;display:flex;height:35px}
.nl-email{flex:1;background:#f2e0c0;border:1px solid #d9bc8c;border-radius:3px 0 0 3px;font-size:14px;color:#9a8a74;line-height:33px;padding-left:9px}
.nl-join{width:62px;background:var(--orange);color:#fff;font-size:15px;line-height:35px;text-align:center;border-radius:0 3px 3px 0}

/* footer */
.footer{left:0;top:1024px;width:1200px;height:67px;background:var(--footer)}
.footer-links{left:209px;top:1047px;font-size:10px;color:#fff}
.footer-links span{margin:0 4px}
.copyright{left:209px;top:1064px;font-size:8px;color:#f7c18a}
.to-top{left:971px;top:1051px;width:20px;height:20px}
</style>
</head>
<body>

<header>
  <div class="abs topbar"></div>
  <div class="abs brand"><span class="brand-dot"></span><span class="brand-name">WillowBendHaven</span></div>
  <div class="abs member-login">Member Login</div>
  <nav class="abs nav">
    <a class="active">Home</a><a>Services</a><a>About Us</a><a>Blog</a><a>Contact</a>
  </nav>
</header>

<section>
  <div class="abs hero"></div>
  <div class="abs hero-photo" role="img" aria-label="Woman measuring her thigh with a tape measure"></div>
  <div class="abs hero-kicker">Transform Your</div>
  <div class="abs hero-title">BODY <span class="amp">&amp;</span> LIFE</div>
  <p class="abs hero-text">Lorem Ipsum is simply dummy text of the printing and typesetting industry. Lorem Ipsum has been the industry's <em>standard dummy text</em> ever since the 2012.</p>
  <div class="abs btn-brochure">Request a Brochure</div>
  <div class="abs thumb t1" role="img" aria-label="Tape measure around a waist"></div>
  <div class="abs thumb t2" role="img" aria-label="Tape measure across a stomach"></div>
  <div class="abs thumb t3" role="img" aria-label="Hands pulling a tape measure"></div>
  <div class="abs thumb t4" role="img" aria-label="Feet standing on bathroom scales"></div>
</section>

<main>
  <div class="abs wood"></div>
  <svg class="abs edge" style="top:506px" viewBox="0 0 1200 8" preserveAspectRatio="none"><polygon fill="#f3d3a0" points="0,8 0,4 4,0 8,4 12,0 16,4 20,0 24,4 1200,4 1200,8"/></svg>

  <div class="abs panel about">
    <h2>Willow Bend</h2>
    <p>Lorem Ipsum is simply dummy text of the printing and typesetting industry. Lorem Ipsum has been the industry's standard dummy text ever since the 1500s, when an unknown printer took a galley of type and scrambled it to make a type specimen book. It has survived not only five centuries.</p>
  </div>

  <div class="abs panel visit">
    <div class="lead">or let us<b>come to you</b></div>
    <div class="abs btn-join-now">JOIN NOW</div>
    <p>Don't have time to come to us, or got kids at home?<br>Let us bring our weight loss retreat to you.</p>
  </div>

  <article class="abs card" style="left:208px">
    <div class="card-head">Blue Mountains Sydney<br>Weight Loss Retreat</div>
    <div class="card-body">
      <div class="card-lead"><span class="card-icon" role="img" aria-label="Bowl of fresh salad"></span><strong>Lorem Ipsum is simply dummy text of the printing</strong></div>
      <p>Contrary to popular belief, Lorem Ipsum is not simply random text It has roots in a piece of classical.</p>
      <p>Latin literature from 45 BC, making it over 2000 years old. Richard om Hallworth, the one and Latin professor.</p>
    </div>
    <div class="card-more">» more</div>
  </article>
  <article class="abs card" style="left:405px">
    <div class="card-head">Central Coast NSW<br>Weight Loss Retreat</div>
    <div class="card-body">
      <div class="card-lead"><span class="card-icon" role="img" aria-label="Glass of juice"></span><strong>Lorem Ipsum is simply dummy text of the printing</strong></div>
      <p>Contrary to popular belief, Lorem Ipsum is not simply random text It has roots in a piece of classical.</p>
      <p>Latin literature from 45 BC, making it over 2000 years old. Richard om Hallworth, the one and Latin professor.</p>
    </div>
    <div class="card-more">» more</div>
  </article>
  <article class="abs card" style="left:602px">
    <div class="card-head">Victoria Weight Loss<br>Health Retreats</div>
    <div class="card-body">
      <div class="card-lead"><span class="card-icon" role="img" aria-label="Fruit pie"></span><strong>Lorem Ipsum is simply dummy text of the printing</strong></div>
      <p>Contrary to popular belief, Lorem Ipsum is not simply random text It has roots in a piece of classical.</p>
      <p>Latin literature from 45 BC, making it over 2000 years old. Richard om Hallworth, the one and Latin professor.</p>
    </div>
    <div class="card-more">» more</div>
  </article>
  <article class="abs card" style="left:800px">
    <div class="card-head single">More Content</div>
    <div class="card-body">
      <div class="card-lead"><span class="card-icon" role="img" aria-label="Slice of layered cake"></span><strong>Lorem Ipsum is simply dummy text of the printing</strong></div>
      <p>Contrary to popular belief, Lorem Ipsum is not simply random text It has roots in a piece of classical.</p>
      <p>Latin literature from 45 BC, making it over 2000 years old. Richard om Hallworth, the one and Latin professor.</p>
    </div>
    <div class="card-more">» more</div>
  </article>

  <div class="abs panel promo">
    <div class="abs promo-inner">
      <div class="abs promo-photo" role="img" aria-label="Pregnant woman holding a green apple"></div>
      <div class="abs promo-title">EATING RIGHT</div>
      <div class="abs promo-sub">When Pregnant</div>
      <svg class="abs ribbon" viewBox="0 0 110 110">
        <polygon points="20,0 48,0 110,62 110,90" fill="#e8650c"/>
        <text x="64" y="43" transform="rotate(45 64 43)" fill="#fff" font-family="Arimo,Arial,sans-serif" font-size="11" text-anchor="middle">SPECIAL</text>
      </svg>
    </div>
  </div>

  <div class="abs panel newsletter">
    <div class="abs newsletter-inner">
      <div class="nl-title"><b>JOIN OUR</b> Weekly Newsletter &amp; Receive</div>
      <div class="nl-sub">Weekly Diet Menu, Health Tips, Special Offers.</div>
      <div class="nl-form"><div class="nl-email">email</div><div class="nl-join">JOIN</div></div>
    </div>
  </div>
</main>

<footer>
  <div class="abs footer"></div>
  <svg class="abs edge" style="top:1018px" viewBox="0 0 1200 8" preserveAspectRatio="none"><polygon fill="#c96612" points="0,8 0,4 1200,4 1200,8"/></svg>
  <div class="abs footer-links">Home<span>|</span>About Us<span>|</span>Services<span>|</span>Contact Us</div>
  <div class="abs copyright">©2012 Willow Bend Haven. All Rights Reserved.</div>
  <svg class="abs to-top" viewBox="0 0 20 20" aria-label="Back to top"><circle cx="10" cy="10" r="10" fill="#e58b3d"/><path d="M10 4 L16 10 H12.5 V16 H7.5 V10 H4 Z" fill="#fff"/></svg>
</footer>

</body>
</html>
```